Dynamic Business Card for Sports Supplements Company

Hi! I'm looking for an awesome business card to match my existing sports supplement company. I have uploaded my current company logo and screenshot of the front page of my website.

I would like to have something dynamic and interesting and utilize the colors in the website - the reds and purples

The business card should be double sided and focus on a unique eye-catching design on the back and include all the relevant company info.

Most importantly, it should say somewhere: "Sign up on our website for a coupon code."

Target Market(s)

Mostly for women gym goers but it shouldn't be too feminine. It should be in keeping with the website design. It should flow and clearly be connected to it

Industry/Entity Type

Business

Contact Information for Business Card

Lorena K. Vasquez
CEO
LVasquez@Fortivanco.example
www.fortivanco.example
614.275.3081
P.O. Box 48317
Alder Falls, Ohio 22417

Sign up on our website for a coupon code

Font styles to use
Serif
Sans Serif
Other font styles liked:
• Novecento font family and "Fortivan" is in AR Destine font

Requirements
Must have
• One side should be a bold Fortivan logo design. Even just the symbol itself may be o.k. (see attached file)

```html
<!DOCTYPE html>
<html lang="en">
<head>
<meta charset="utf-8">
<title>Fortivan Business Card</title>
<link href="https://fonts.googleapis.com/css2?family=Montserrat:wght@400;500;600;700;800&display=swap" rel="stylesheet">
<style>
  :root {
    --stage: #3a3a3a;
    --ink: #111111;
    --paper: #ffffff;
    --brand-red: #e3242b;
    --text-grey: #6b6b6b;
    --rule: #555555;
    --card-w: 560px;
    --card-h: 320px;
  }
  * { box-sizing: border-box; margin: 0; padding: 0; }
  html, body {
    width: 1200px; height: 855px; overflow: hidden;
    background: var(--stage);
    font-family: "Montserrat", Arial, sans-serif;
  }
  .stage {
    width: 1200px; height: 855px;
    display: flex; align-items: center; justify-content: center; gap: 30px;
  }
  .card {
    width: var(--card-w); height: var(--card-h);
    position: relative;
    box-shadow: 0 10px 30px rgba(0,0,0,.45);
  }
  /* Back side */
  .card-back {
    background: var(--ink); color: var(--paper);
    display: flex; flex-direction: column; align-items: center;
  }
  .brand {
    display: flex; flex-direction: column; align-items: center;
  }
  .card-back .brand { margin-top: 96px; }
  .brand-row { display: flex; align-items: center; gap: 10px; }
  .brand-mark {
    width: 22px; height: 22px; background: var(--brand-red);
  }
  .brand-name {
    font-weight: 800; font-size: 38px; letter-spacing: 2px;
    text-transform: uppercase; line-height: 1;
  }
  .brand-tagline {
    font-weight: 500; font-size: 11px; letter-spacing: 2.4px;
    text-transform: uppercase; margin-top: 6px;
  }
  .coupon-line {
    position: absolute; bottom: 52px; left: 0; right: 0;
    text-align: center; font-size: 13px; font-weight: 500; letter-spacing: .6px;
  }
  .coupon-line .accent { color: var(--brand-red); }

  /* Front side */
  .card-front {
    background: var(--paper); color: var(--ink);
    display: flex; align-items: center;
  }
  .card-front .brand { width: 252px; margin-left: 18px; }
  .card-front .brand-name { font-size: 30px; }
  .card-front .brand-tagline { font-size: 9px; letter-spacing: 2px; }
  .divider {
    width: 1.5px; height: 150px; background: var(--rule);
    margin: 0 22px 0 12px;
  }
  .contact { display: flex; flex-direction: column; }
  .person-name { font-weight: 600; font-size: 18px; }
  .person-role { font-size: 13px; color: var(--text-grey); margin-top: 2px; }
  .address {
    font-size: 13px; color: var(--text-grey); line-height: 1.35;
    margin-top: 14px; margin-left: 8px;
  }
  .details { list-style: none; margin-top: 12px; margin-left: 14px; }
  .details li {
    display: flex; align-items: center; gap: 8px;
    font-size: 12.5px; color: var(--text-grey); line-height: 1.45;
  }
  .details svg { width: 11px; height: 11px; flex: none; }
</style>
</head>
<body>
<main class="stage">
  <section class="card card-back" aria-label="Card back">
    <div class="brand">
      <div class="brand-row">
        <span class="brand-mark"></span>
        <span class="brand-name">Fortivan</span>
      </div>
      <span class="brand-tagline">Your Performance Partner</span>
    </div>
    <p class="coupon-line">Sign up on our website <span class="accent">for a coupon code</span></p>
  </section>

  <section class="card card-front" aria-label="Card front">
    <div class="brand">
      <div class="brand-row">
        <span class="brand-mark"></span>
        <span class="brand-name">Fortivan</span>
      </div>
      <span class="brand-tagline">Your Performance Partner</span>
    </div>
    <div class="divider"></div>
    <div class="contact">
      <h1 class="person-name">Lorena K. Vasquez</h1>
      <p class="person-role">CEO</p>
      <p class="address">P.O. Box 48317<br>Alder Falls, Ohio 22417</p>
      <ul class="details">
        <li>
          <svg viewBox="0 0 12 12" aria-hidden="true"><path d="M2.5 1 L4.5 1 L5 3.5 L3.8 4.5 C4.5 6 6 7.5 7.5 8.2 L8.5 7 L11 7.5 L11 9.5 C11 10.3 10.3 11 9.5 11 C5 11 1 7 1 2.5 C1 1.7 1.7 1 2.5 1Z" fill="var(--brand-red)"/></svg>
          614.275.3081
        </li>
        <li>
          <svg viewBox="0 0 12 12" aria-hidden="true"><rect x="0.5" y="2" width="11" height="8" fill="var(--brand-red)"/><path d="M0.5 2 L6 6.5 L11.5 2" stroke="#fff" stroke-width="1" fill="none"/></svg>
          LVasquez@Fortivanco.example
        </li>
        <li>
          <svg viewBox="0 0 12 12" aria-hidden="true"><g fill="none" stroke="var(--brand-red)" stroke-width="1.1"><circle cx="6" cy="6" r="5"/><ellipse cx="6" cy="6" rx="2.2" ry="5"/><path d="M1 6 H11 M2 3.4 H10 M2 8.6 H10"/></g></svg>
          www.fortivanco.example
        </li>
      </ul>
    </div>
  </section>
</main>
</body>
</html>
```